Membership Drive "CHRISTMAS SPECIAL"

Looking to run a "Christmas Special" on 6 month Memberships for December 2019 to boost membership number up. This is a great time to get people exercising and everyone loves a Christmas Sale. Special is designed to attract more people to join and enjoy the savings.
Artwork will be display via social media (PX and Pictoria) as well as in store. Artwork must be eye catching and direct to the customer. Customer should feel a sense of relief with being able to exercise at a lower cost .

Heading: "Christmas Sale"
6 Months
$199.00 Save over 30%
Terms and conditions apply"
*Offer End 31st December

below are other promos we had designed on Sketch Harbor along with potential photos to be included into this promo

Target Market(s)

Males and Females aged between 16 - 45

Industry/Entity Type

Fitness

Colors

Designer to choose colors to be used in the design.

Requirements
Must have
• Must emphasize "Christmas Special" $199.00 Save over 30%
• Terms and conditions apply
• Offer Ends 31st of December
• "All of our contact details"
• Address: 14 Wattle Rd Greenfield Park 3051
• Ph: 9482 6107
• www.summitfitclub.com.au
• Design format must come in PDF for a AO poster and an Pictoria format please
Nice to have
• Some Christmas feels to the artwork

```html
<!DOCTYPE html>
<html lang="en">
<head>
<meta charset="utf-8">
<title>Christmas Special – Summit Fit Club</title>
<link rel="stylesheet" href="https://fonts.googleapis.com/css2?family=Graduate&family=Exo+2:wght@400;500;800&family=Oswald:wght@700&display=swap">
<style>
  :root {
    --page-bg: #e8e8e8;
    --red-light: #951b1b;
    --red-mid: #7a1010;
    --red-dark: #560808;
    --band-red: #7c0b0b;
    --yellow: #ffcb05;
    --title-red: #8e1115;
    --ink: #111111;
    --white: #ffffff;
  }
  * { margin: 0; padding: 0; box-sizing: border-box; }
  html, body { width: 879px; height: 1200px; overflow: hidden; }
  body { background: var(--page-bg); position: relative; }

  .poster {
    position: absolute; left: 102px; top: 0;
    width: 675px; height: 1200px; overflow: hidden;
    background: radial-gradient(ellipse at 60% 40%, var(--red-light) 0%, var(--red-mid) 55%, var(--red-dark) 100%);
  }
  .brush { position: absolute; }
  .brush svg { display: block; width: 100%; height: 100%; }

  .title-brush { left: 30px; top: 56px; width: 595px; height: 232px; }
  .title {
    position: absolute; left: 30px; top: 76px; width: 595px;
    text-align: center; font-family: "Graduate", serif;
    color: var(--title-red); font-size: 78px; line-height: 84px;
    transform: scaleX(0.86); letter-spacing: -1px;
  }

  .photo {
    position: absolute; left: 0; top: 326px; width: 400px; height: 702px;
    background: linear-gradient(160deg, #e9dcd4 0%, #c9a089 22%, #6b3a28 50%, #b8141b 78%, #8e0d12 100%);
    opacity: 0.92;
  }

  .save {
    position: absolute; left: 392px; top: 306px; width: 262px;
    font-family: "Exo 2", sans-serif; font-weight: 400; color: var(--white);
    font-size: 46px; line-height: 46px; letter-spacing: 18px;
  }
  .percent {
    position: absolute; left: 386px; top: 392px;
    font-family: "Exo 2", sans-serif; font-weight: 800; color: var(--white);
    font-size: 110px; line-height: 110px; letter-spacing: -2px;
  }

  .price-brush { left: 360px; top: 516px; width: 315px; height: 160px; }
  .months {
    position: absolute; left: 398px; top: 534px;
    font-family: "Exo 2", sans-serif; font-weight: 500; color: var(--ink);
    font-size: 32px; letter-spacing: 5px; line-height: 36px;
  }
  .price {
    position: absolute; left: 394px; top: 572px;
    font-family: "Oswald", sans-serif; font-weight: 700; color: var(--ink);
    font-size: 76px; line-height: 88px; letter-spacing: -1px;
  }

  .note {
    position: absolute; right: 39px; width: 260px; text-align: right;
    font-family: "Exo 2", sans-serif; color: var(--white);
    font-size: 22px; line-height: 29px;
  }
  .note-terms { top: 728px; }
  .note-ends { top: 828px; }

  .contact-band {
    position: absolute; left: 0; top: 1028px; width: 675px; height: 172px;
    background: var(--band-red);
  }
  .brand {
    position: absolute; left: 52px; top: 1088px; width: 210px;
    font-family: "Exo 2", sans-serif; font-weight: 800; color: var(--white);
    font-size: 30px; line-height: 32px; letter-spacing: 1px;
  }
  .contacts {
    position: absolute; left: 285px; top: 1064px;
    font-family: "Exo 2", sans-serif; color: var(--white);
    font-size: 22px; line-height: 40px;
    list-style: none;
  }
</style>
</head>
<body>
  <main class="poster">
    <div class="photo" role="img" aria-label="Photo of a smiling woman in a red and white Santa outfit holding a red dumbbell"></div>

    <div class="brush title-brush">
      <svg viewBox="0 0 595 232" preserveAspectRatio="none" aria-hidden="true">
        <path fill="var(--yellow)" d="M28 18 L120 10 L260 14 L400 6 L540 12 L560 24 L548 34 L575 46 L562 62 L585 78 L570 96 L590 114 L572 132 L584 150 L566 168 L580 186 L556 200 L420 206 L300 212 L180 216 L80 224 L40 228 L36 212 L14 202 L30 186 L8 170 L26 150 L4 132 L22 112 L0 96 L24 78 L6 60 L30 44 L12 30 Z"/>
      </svg>
    </div>
    <h1 class="title">CHRISTMAS<br>SPECIAL</h1>

    <p class="save">SAVE<br>OVER</p>
    <p class="percent">30%</p>

    <div class="brush price-brush">
      <svg viewBox="0 0 315 160" preserveAspectRatio="none" aria-hidden="true">
        <path fill="var(--yellow)" d="M20 8 L140 4 L315 10 L315 60 L304 70 L315 84 L308 104 L315 118 L292 132 L200 140 L90 146 L40 156 L30 140 L12 130 L26 116 L4 100 L22 84 L8 66 L24 50 L10 32 L26 20 Z"/>
      </svg>
    </div>
    <p class="months">6 MONTHS</p>
    <p class="price">$199.00</p>

    <p class="note note-terms">Terms and<br>conditions apply</p>
    <p class="note note-ends">Offer Ends<br>31st of December</p>

    <footer class="contact-band"></footer>
    <p class="brand">SUMMIT<br>FIT CLUB</p>
    <ul class="contacts">
      <li>14 Wattle Rd Greenfield Park 3051</li>
      <li>9482 6107</li>
      <li>www.summitfitclub.com.au</li>
    </ul>
  </main>
</body>
</html>
```